Northgate Roofing Works Inc Business cards

Commercial and Residential Roofing contractor needs design logo and card design. Can be single or double sided but must incorporate:
Persons Name:
Persons Title:
Mailing Address: PO Box 3719
Physical Address: 58 Fenwick Lane
Hollis Falls, Ma. 01488
800-316-5842
508-712-5842
Fax: 508-712-5867
Cell: Person Cell number
email address
Website: WWW.northgateroofworks.com

Target Market(s)

Residential home owners and commercial building owners

Industry/Entity Type

Roofing

Contact Information for Business Card

Persons Name:
Persons Title:
Hollis Falls, Ma. 01488
800-316-5842
508-712-5842
Fax: 508-712-5867
Cell: Person Cell number
email address

Logo Text

Large enough to service small enough to care

Font styles to use
Serif

Colors
0355a3

Requirements
Must have
• Commercial and Residential Roofing contractor needs design logo and card design. Can be single or double sided but must incorporate:
• Persons Name:
• Persons Title:
• Mailing Address: PO Box 3719
• Physical Address: 58 Fenwick Lane
• Hollis Falls, Ma. 01488
• 800-316-5842
• 508-712-5842
• Fax: 508-712-5867
• Cell: Person Cell number
• email address
• Website: WWW.northgateroofworks.com
Nice to have
• ..
Should not have
• I'm looking for something different. I have had the same card for 23 years. I attached what both sides of my present card looks like.

```html
<!DOCTYPE html>
<html lang="en">
<head>
<meta charset="utf-8">
<title>Northgate Roofing Works Inc – Business Cards</title>
<link rel="stylesheet" href="https://fonts.googleapis.com/css2?family=Josefin+Sans:wght@400;700&family=Questrial&display=swap">
<style>
  :root {
    --backdrop: #d6d6d6;
    --card: #ffffff;
    --band: #ebebeb;
    --ink: #1d1d1d;
    --ink-soft: #4a4a4a;
    --accent: #5cc4c6;
    --tab: #2b2b2b;
  }
  * { margin: 0; padding: 0; box-sizing: border-box; }
  html, body { width: 1200px; height: 800px; overflow: hidden; }
  body { background: var(--backdrop); position: relative; font-family: "Questrial", sans-serif; color: var(--ink); }

  .card { position: absolute; top: 272px; height: 263px; background: var(--card); overflow: hidden; }
  .card--front { left: 60px; width: 480px; }
  .card--back { left: 640px; width: 500px; }

  .hatch-band { position: absolute; background: var(--band); }
  .card--front .hatch-band--top { left: 0; top: 0; width: 100%; height: 34px; }
  .card--front .hatch-band--bottom { left: 0; bottom: 0; width: 100%; height: 35px; }
  .card--back .hatch-band--column { left: 30px; top: 0; width: 195px; height: 100%; }

  .brand { position: absolute; display: flex; align-items: center; }
  .brand__mark { background: var(--accent); flex: none; }
  .brand__name { font-family: "Josefin Sans", sans-serif; font-weight: 700; color: var(--ink); text-transform: uppercase; line-height: 1.05; }

  .card--front .brand { left: 85px; top: 87px; gap: 14px; }
  .card--front .brand__mark { width: 80px; height: 80px; }
  .card--front .brand__name { font-size: 32px; }

  .card--back .brand { left: 41px; top: 99px; gap: 8px; }
  .card--back .brand__mark { width: 46px; height: 46px; }
  .card--back .brand__name { font-size: 17px; }

  .contact-rule { position: absolute; left: 236px; top: 85px; width: 3px; height: 94px; background: var(--ink); }
  .contact { position: absolute; left: 253px; top: 72px; }
  .contact__name { font-family: "Josefin Sans", sans-serif; font-weight: 400; font-size: 19px; letter-spacing: 1.5px; text-transform: uppercase; line-height: 1; }
  .contact__title { font-size: 9px; color: var(--ink-soft); margin-top: 5px; }
  .contact__details { list-style: none; margin-top: 10px; font-size: 8.3px; line-height: 10.4px; color: var(--ink-soft); }

  .edge-tab { position: absolute; right: 27px; top: 85px; width: 30px; height: 93px; background: var(--tab); }
</style>
</head>
<body>

  <section class="card card--front" aria-label="Card front">
    <div class="hatch-band hatch-band--top" role="img" aria-label="Light grey diagonal hatch band"></div>
    <div class="brand">
      <span class="brand__mark"></span>
      <span class="brand__name">Northgate<br>Roofing<br>Works Inc</span>
    </div>
    <div class="hatch-band hatch-band--bottom" role="img" aria-label="Light grey diagonal hatch band"></div>
  </section>

  <section class="card card--back" aria-label="Card back">
    <div class="hatch-band hatch-band--column" role="img" aria-label="Light grey diagonal hatch column"></div>
    <div class="brand">
      <span class="brand__mark"></span>
      <span class="brand__name">Northgate<br>Roofing<br>Works Inc</span>
    </div>
    <div class="contact-rule"></div>
    <div class="contact">
      <p class="contact__name">Daniel Mercer</p>
      <p class="contact__title">CEO</p>
      <ul class="contact__details">
        <li>Mailing Address: PO Box 3719</li>
        <li>Physical Address: 58 Fenwick Lane</li>
        <li>Hollis Falls, Ma. 01488</li>
        <li>800-316-5842</li>
        <li>508-712-5842</li>
        <li>Fax: 508-712-5867</li>
        <li>Cell: Person Cell number</li>
        <li>email address</li>
        <li>Website: WWW.northgateroofworks.com</li>
      </ul>
    </div>
    <div class="edge-tab"></div>
  </section>

</body>
</html>
```